New Business Card for Innovative Tool Company

We need a new design of business card for our florida based tool manufacturing company. I will attach 2 files that we use for our logo, use whichever you feel works best for the card. Main colours are as per logo, and we can use different shades of black/white/grey for the background.

Contact Information for Business Card

Name/Jobtitle/cell
Corvalen Tools
Suite 212c
4316 Marrowdale Pkw
Orlando, FL32847
USA
name@corvaleninc.example
www.corvaleninc.example

Font styles to use
Sans Serif

Colors

Designer to choose colors to be used in the design.

Requirements
Must have
• Icons for Plazaro, Chirpet, Snapvale, Findlo & Vidstream

```html
<!DOCTYPE html>
<html lang="en">
<head>
<meta charset="utf-8">
<title>Corvalen Tools – Business Card</title>
<link rel="stylesheet" href="https://fonts.googleapis.com/css2?family=Montserrat:wght@400;500;700;800&display=swap">
<style>
  :root {
    --stage: #2b2b2b;
    --card: #1c1c1c;
    --card-edge: #141414;
    --gloss: #3b3b3b;
    --yellow: #f2e21c;
    --white: #f2f2f2;
    --muted: #d9d9d9;
    --emboss: #262626;
  }
  * { box-sizing: border-box; margin: 0; padding: 0; }
  html, body { width: 1200px; height: 863px; overflow: hidden; background: var(--stage); font-family: "Montserrat", sans-serif; }
  .canvas { position: relative; width: 1200px; height: 863px; }

  .card {
    position: absolute; width: 525px; height: 300px;
    background: var(--card); border-radius: 4px;
    box-shadow: 0 10px 30px rgba(0,0,0,.55);
    overflow: hidden;
  }
  .card--front { left: 45px; top: 110px; }
  .card--back  { left: 630px; top: 450px; }

  /* Front */
  .front-brand {
    position: absolute; left: 0; right: 0; top: 92px;
    display: flex; align-items: center; justify-content: center; gap: 14px;
  }
  .front-brand__mark { width: 46px; height: 46px; border: 2px solid var(--gloss); border-radius: 50%; }
  .front-brand__name {
    font-weight: 800; font-size: 38px; letter-spacing: 3px; color: var(--gloss);
    text-transform: uppercase;
  }
  .social-row {
    position: absolute; left: 0; right: 0; top: 205px;
    display: flex; justify-content: center; gap: 16px; list-style: none;
  }
  .social-row__item { display: flex; align-items: center; gap: 5px; color: var(--yellow); font-size: 11px; font-weight: 500; }
  .social-row__dot { width: 14px; height: 14px; border: 1.5px solid var(--yellow); border-radius: 50%; }

  /* Back */
  .back-brand {
    position: absolute; right: 34px; top: 28px;
    font-weight: 800; font-size: 30px; letter-spacing: 2px; color: var(--yellow); text-transform: uppercase;
  }
  .back-deco { position: absolute; right: -70px; bottom: -150px; width: 330px; height: 330px; border: 2px solid var(--emboss); border-radius: 50%; }
  .person { position: absolute; left: 32px; top: 92px; }
  .person__name { font-weight: 700; font-size: 20px; color: var(--yellow); }
  .person__role { font-size: 12px; color: var(--muted); margin-top: 2px; }
  .contact { position: absolute; left: 32px; top: 160px; list-style: none; }
  .contact__line { display: flex; align-items: center; gap: 8px; font-size: 12.5px; color: var(--white); line-height: 20px; }
  .contact__icon { width: 12px; height: 12px; fill: none; stroke: var(--yellow); stroke-width: 1.4; }
  .address { position: absolute; left: 32px; top: 232px; font-size: 12.5px; line-height: 19px; color: var(--white); font-style: normal; }
</style>
</head>
<body>
<main class="canvas">

  <section class="card card--front" aria-label="Card front">
    <div class="front-brand">
      <span class="front-brand__mark"></span>
      <span class="front-brand__name">Corvalen Tools</span>
    </div>
    <ul class="social-row">
      <li class="social-row__item"><span class="social-row__dot"></span>Plazaro</li>
      <li class="social-row__item"><span class="social-row__dot"></span>Chirpet</li>
      <li class="social-row__item"><span class="social-row__dot"></span>Findlo</li>
      <li class="social-row__item"><span class="social-row__dot"></span>Snapvale</li>
      <li class="social-row__item"><span class="social-row__dot"></span>Vidstream</li>
    </ul>
  </section>

  <section class="card card--back" aria-label="Card back">
    <div class="back-deco"></div>
    <div class="back-brand">Corvalen Tools</div>
    <div class="person">
      <p class="person__name">Dorian HALE</p>
      <p class="person__role">Managing Director</p>
    </div>
    <ul class="contact">
      <li class="contact__line">
        <svg class="contact__icon" viewBox="0 0 12 12"><path d="M3 1l2 2.5-1.2 1.2c.6 1.3 1.6 2.3 2.9 2.9L8 6.4 10.5 8.5 9.3 10.8C5 10.5 1.5 7 1.2 2.7z"/></svg>
        000 000 0000
      </li>
      <li class="contact__line">
        <svg class="contact__icon" viewBox="0 0 12 12"><rect x="1" y="2.5" width="10" height="7"/><path d="M1 2.5l5 4 5-4"/></svg>
        name@corvaleninc.example
      </li>
      <li class="contact__line">
        <svg class="contact__icon" viewBox="0 0 12 12"><circle cx="6" cy="6" r="5"/><path d="M1 6h10M6 1c2.5 2.8 2.5 7.2 0 10M6 1c-2.5 2.8-2.5 7.2 0 10"/></svg>
        www.corvaleninc.example
      </li>
    </ul>
    <address class="address">
      Suite 212c, 4316 Marrowdale Pkw<br>
      Orlando, FL32847, USA
    </address>
  </section>

</main>
</body>
</html>
```